Luxury Candle Startup Needs Modern Packaging Box & Matching Label Design

We are Lunavale, a luxury candle company about to launch in Australia and we need a box packaging design that is modern, minimalist, and feminine. Our target audience are females, mostly mothers, within the age range of 25-45 who are looking for high quality, handmade luxurious products. Our company is going to have a large social media presence with new mothers as we are going to show our journey with starting a business whilst on maternity leave. We would like the arch shape incorporated into the box packaging as it is beautiful and symbolises moving into a new phase in life which really represents the brand. We would like for the packaging box to be a simple white box with a sleeve insert over the box with the design to make printing easier. Our colour inspiration are very earthy colours and would like the sleeve colour to be easily changed according to the scent. For example dusky rose coloured sleeve for rose patchouli and amber scent, light coffee coloured sleeve for coffee bean cacao scent etc. Please see uploaded files for inspiration, our logo, and the type of candle jars used.
The box dimensions are:
External Dimension: 95mmW x 95mmL x 116mmH
We look forward to seeing your amazing designs!

```html
<!DOCTYPE html>
<html lang="en">
<head>
<meta charset="utf-8">
<title>Lunavale – Candle Box Dieline, Sleeve &amp; Label</title>
<link href="https://fonts.googleapis.com/css2?family=Josefin+Sans:wght@300;400&family=Allura&display=swap" rel="stylesheet">
<style>
  :root {
    --backdrop: #8f8e87;
    --board: #ffffff;
    --pattern-tone: #ececec;
    --sleeve-rose: #dbbdb6;
    --foil-gold: #ecd29c;
    --logo-grey: #cdcdcd;
    --copy-grey: #b9b9b9;
  }
  html, body {
    margin: 0;
    padding: 0;
    width: 729px;
    height: 1200px;
    overflow: hidden;
    background: var(--backdrop);
  }
  .artboard {
    position: relative;
    width: 729px;
    height: 1200px;
  }
  .dieline {
    position: absolute;
    left: 0;
    top: 268px;
    width: 729px;
    height: 664px;
  }
  .board { fill: var(--board); }
  .pattern { fill: var(--pattern-tone); }
  .sleeve { fill: var(--sleeve-rose); }
  .wordmark {
    font-family: "Josefin Sans", sans-serif;
    font-weight: 300;
    letter-spacing: 2px;
    text-anchor: middle;
  }
  .caps {
    font-family: "Josefin Sans", sans-serif;
    font-weight: 400;
    text-anchor: middle;
  }
  .script {
    font-family: "Allura", cursive;
    text-anchor: middle;
  }
  .on-white { fill: var(--logo-grey); }
  .copy { fill: var(--copy-grey); }
  .on-rose { fill: var(--foil-gold); }
  .foil-rule { stroke: var(--foil-gold); stroke-width: 1.6; fill: none; }
</style>
</head>
<body>
<main class="artboard">
  <svg class="dieline" viewBox="100 1180 1170 1065" xmlns="http://www.w3.org/2000/svg">
    <!-- glue flap -->
    <path class="board glue-flap" d="M178 1520 L122 1538 Q108 1544 108 1558 L108 1826 Q108 1838 122 1842 L178 1848 Z"/>

    <!-- front panel with tuck flap -->
    <path class="board front-panel" d="M178 1848 L178 1225 Q178 1195 208 1195 L418 1195 Q448 1195 448 1225 L448 1848 Z"/>
    <g class="front-pattern" role="img" aria-label="Light grey mandala lace pattern around an arch">
      <path class="pattern" d="M178 1250 H448 V1670 H375 V1596 A61.5 61.5 0 0 0 252 1596 V1670 H178 Z"/>
      <path class="pattern" d="M178 1757 H252 V1848 H178 Z M375 1757 H448 V1848 H375 Z"/>
    </g>
    <text class="wordmark on-white" x="313" y="1710" font-size="28">LUNAVALE</text>
    <text class="caps copy" x="313" y="1728" font-size="10" letter-spacing="2.5">LUXURY FRAGRANCE</text>
    <text class="caps copy" x="313" y="1742" font-size="7.5" letter-spacing="2">AUSTRALIA</text>

    <!-- side panel with dust flaps -->
    <path class="board side-panel" d="M448 1848 L448 1340 Q448 1328 460 1328 L640 1328 Q652 1328 656 1340 L690 1440 L718 1475 L718 2040 L522 2040 Q510 2040 506 2028 L478 1930 L448 1890 Z"/>
    <text class="caps copy" x="583" y="1716" font-size="13" letter-spacing="4">SOY CANDLE</text>
    <text class="script copy" x="583" y="1731" font-size="14">Hand Poured</text>

    <!-- back panel with bottom tuck -->
    <path class="board back-panel" d="M718 1520 H986 V2210 Q986 2240 956 2240 H748 Q718 2240 718 2210 Z"/>
    <g class="back-pattern" role="img" aria-label="Light grey mandala lace pattern">
      <rect class="pattern" x="718" y="1520" width="268" height="150"/>
      <rect class="pattern" x="718" y="1757" width="268" height="91"/>
    </g>

    <!-- side panel with dust flaps -->
    <path class="board side-panel" d="M986 1520 L986 1475 L1014 1440 L1048 1340 Q1052 1328 1064 1328 L1256 1328 L1256 1890 L1226 1930 L1198 2028 Q1194 2040 1182 2040 L986 2040 Z"/>
    <text class="caps copy" x="1125" y="1714" font-size="7" letter-spacing="1.5">300GRAMS</text>
    <text class="caps copy" x="1125" y="1727" font-size="7" letter-spacing="1.5">50 HOUR BURN TIME</text>

    <!-- scent sleeve -->
    <rect class="sleeve scent-sleeve" x="759" y="1235" width="184" height="995"/>
    <text class="wordmark on-rose" x="851" y="1710" font-size="23">LUNAVALE</text>
    <text class="caps on-rose" x="851" y="1727" font-size="7" letter-spacing="1.8">LUXURY FRAGRANCE</text>
    <text class="caps on-rose" x="851" y="1738" font-size="5.5" letter-spacing="1.5">AUSTRALIA</text>
    <line class="foil-rule" x1="838" y1="1772" x2="866" y2="1772"/>
    <text class="caps on-rose" x="851" y="1797" font-size="8.5" letter-spacing="2">ROSE PATCHOULI</text>

    <!-- arch label -->
    <path class="sleeve arch-label" d="M230 2195 V2005 A83.5 83.5 0 0 1 397 2005 V2195 Z"/>
    <path class="foil-rule" stroke-width="1" d="M238 2187 V2008 A75.5 75.5 0 0 1 389 2008 V2187 Z"/>
    <text class="wordmark on-rose" x="313.5" y="2089" font-size="15" letter-spacing="1">LUNAVALE</text>
    <text class="caps on-rose" x="313.5" y="2100" font-size="4.5" letter-spacing="1">LUXURY FRAGRANCE</text>
    <text class="caps on-rose" x="313.5" y="2107" font-size="3.8" letter-spacing="1">AUSTRALIA</text>
    <text class="caps on-rose" x="313.5" y="2139" font-size="6" letter-spacing="1.2">ROSE PATCHOULI</text>
  </svg>
</main>
</body>
</html>
```